Natural Health Supplement Company Needs a Product Label Designed

HARVEST ROOT LABS needs a PROBIOTICS product label designed.We are a natural health vitamin and dietary supplement company. Who ever wins will have the opportunity to design a lot more product labels for us.
Product name: PROBIOTICS
*Please use the attached logo and base the label text exactly off the Kelt Wellness label example.
Other product examples have been attached for inspiration.

Colors

Designer to choose colors to be used in the design.

Requirements
Must have
• Product name: PROBIOTICS
• *Please use the attached logo and base the label text exactly off the Kelt Wellness label example.
• Other product examples have been attached for inspiration.

```html
<!DOCTYPE html>
<html lang="en">
<head>
<meta charset="utf-8">
<title>Harvest Root Labs – Probiotic-40 Label</title>
<link rel="stylesheet" href="https://fonts.googleapis.com/css2?family=Open+Sans:ital,wght@0,400;0,600;0,700;0,800;1,400;1,600&display=swap">
<style>
  :root {
    --label-white: #ffffff;
    --page-bg: #eef0f2;
    --navy: #4c5f84;
    --navy-dark: #3c4d6e;
    --navy-light: #6d7fa3;
    --green: #8cc652;
    --green-light: #b3dd88;
    --green-dark: #6aa33c;
    --grey-tab: #7d7f82;
    --pattern-tone: #e7ebf2;
    --accent-blue: #3a9ad9;
    --badge-red: #e05a5a;
    --badge-gold: #f5c431;
  }
  html, body {
    margin: 0;
    padding: 0;
    width: 1045px;
    height: 1200px;
    overflow: hidden;
    background: var(--page-bg);
  }
  .label {
    position: relative;
    width: 1045px;
    height: 1200px;
    background: var(--label-white);
    overflow: hidden;
    font-family: "Open Sans", sans-serif;
  }
  .label-shapes {
    position: absolute;
    inset: 0;
  }
  .count-tab {
    position: absolute;
    left: 815px;
    top: 70px;
    width: 185px;
    text-align: center;
    color: var(--label-white);
    line-height: 1;
  }
  .count-tab .count-number { font-size: 92px; font-weight: 800; letter-spacing: -2px; }
  .count-tab .count-unit { font-size: 21px; font-weight: 400; letter-spacing: 1px; margin-top: 4px; }
  .count-tab .count-claim { font-size: 25px; font-weight: 800; margin-top: 8px; line-height: 1.05; }
  .count-tab .count-claim span { letter-spacing: 9px; display: block; }

  .brand {
    position: absolute;
    left: 0;
    width: 710px;
    top: 220px;
    text-align: center;
  }
  .brand-dot {
    width: 110px;
    height: 110px;
    border-radius: 50%;
    background: var(--green);
    margin: 0 auto 38px;
  }
  .brand-name {
    font-size: 58px;
    font-weight: 600;
    color: var(--green);
    letter-spacing: 3px;
  }

  .product-title {
    position: absolute;
    left: 450px;
    top: 755px;
    color: var(--label-white);
    font-weight: 700;
    line-height: 1.08;
    transform: rotate(-3deg);
    transform-origin: left top;
  }
  .product-title .title-line { font-size: 80px; letter-spacing: 1px; }
  .product-title .dose { font-size: 30px; font-style: italic; color: var(--accent-blue); margin-left: 12px; }

  .tech-line {
    position: absolute;
    left: 318px;
    top: 958px;
    color: var(--label-white);
    font-size: 40px;
    font-style: italic;
    transform: rotate(-4deg);
    transform-origin: left top;
    white-space: nowrap;
  }
  .tech-line .tech-name { font-style: normal; }
  .tech-line sup { font-size: 20px; }

  .benefits {
    position: absolute;
    right: 45px;
    top: 1070px;
    width: 520px;
    text-align: right;
    color: var(--label-white);
    font-size: 17px;
    font-style: italic;
    line-height: 1.2;
    transform: rotate(-4deg);
    transform-origin: right top;
  }
  .benefits p { margin: 0 0 12px; }

  .bestseller {
    position: absolute;
    left: 66px;
    top: 895px;
    width: 180px;
    height: 180px;
    border-radius: 50%;
    background: var(--badge-gold);
    display: flex;
    align-items: center;
    justify-content: center;
  }
  .bestseller-core {
    width: 146px;
    height: 146px;
    border-radius: 50%;
    background: var(--badge-red);
    color: var(--label-white);
    display: flex;
    flex-direction: column;
    align-items: center;
    justify-content: center;
    font-weight: 700;
    line-height: 1;
    transform: rotate(8deg);
  }
  .bestseller-core .best { font-size: 40px; }
  .bestseller-core .seller { font-size: 30px; font-weight: 600; }
</style>
</head>
<body>
<main class="label">
  <svg class="label-shapes" width="1045" height="1200" viewBox="0 0 1045 1200">
    <defs>
      <linearGradient id="pattern-fade" x1="0" y1="0" x2="1" y2="1">
        <stop offset="0" stop-color="#f6f8fb"/>
        <stop offset="0.5" stop-color="var(--pattern-tone)"/>
        <stop offset="1" stop-color="#f6f8fb"/>
      </linearGradient>
      <linearGradient id="navy-sheen" x1="0" y1="1" x2="1" y2="0">
        <stop offset="0" stop-color="var(--navy-dark)"/>
        <stop offset="1" stop-color="var(--navy-light)"/>
      </linearGradient>
    </defs>

    <rect class="hex-pattern" x="0" y="110" width="1045" height="900" fill="url(#pattern-fade)" role="img" aria-label="Faint hexagonal honeycomb background pattern"/>

    <polygon class="top-band-dark" points="0,10 1045,0 1045,30 0,45" fill="var(--green-dark)"/>
    <polygon class="top-band" points="0,45 1045,30 1045,90 0,120" fill="var(--green)"/>
    <polygon class="top-band-light" points="0,55 1045,38 1045,58 0,78" fill="var(--green-light)" opacity="0.6"/>

    <polygon class="corner-wedge" points="0,150 150,142 125,232 0,268" fill="var(--navy)"/>

    <polygon class="count-tab-shape" points="830,55 1000,50 1000,290 815,290 815,75" fill="var(--grey-tab)"/>
    <polygon class="count-tab-fold" points="1000,50 1045,45 1045,85 1000,90" fill="#5f6164"/>

    <polygon class="title-panel" points="511,660 1045,455 1045,1200 255,1200" fill="url(#navy-sheen)"/>
    <polygon class="title-panel-shade" points="511,660 1045,455 1045,520 600,690" fill="var(--navy-dark)" opacity="0.45"/>

    <polygon class="tech-band-fold" points="297,945 340,930 340,965 297,975" fill="var(--green-dark)"/>
    <polygon class="tech-band" points="297,960 1045,900 1045,978 297,1035" fill="var(--green)"/>
  </svg>

  <div class="count-tab">
    <div class="count-number">50</div>
    <div class="count-unit">CAPSULES</div>
    <div class="count-claim">GLUTEN<span>FREE</span></div>
  </div>

  <div class="brand">
    <div class="brand-dot"></div>
    <div class="brand-name">HARVEST ROOT LABS</div>
  </div>

  <div class="product-title">
    <div class="title-line">PROBIOTIC-40</div>
    <div class="title-line">40 BILLION<span class="dose">200mg</span></div>
  </div>

  <div class="tech-line"><span class="tech-name">VELTRA<sup>®</sup></span> Bi-Pass Technology</div>

  <div class="benefits">
    <p>Works naturally with your body to keep your digestive system in balance</p>
    <p>Helps with occasional digestive upset, including diarrhea, gas and bloating</p>
  </div>

  <div class="bestseller">
    <div class="bestseller-core">
      <span class="best">BEST</span>
      <span class="seller">SELLER</span>
    </div>
  </div>
</main>
</body>
</html>
```